Long term design collaboration - mobile app design & web app design

We are looking for a talented mobile designer to help us improve our UI & UX for mobile app and web app.

The screens that need to be redesigned are attached.

There is potentially a lot more work in future design available for the successful candidate.
The successful candidate would have to take part in daily stand-up around 3 times per week.
The successful candidate would join a dev team
We are software company that does property management

```html
<!DOCTYPE html>
<html lang="en">
<head>
<meta charset="utf-8">
<title>Development Overview – Screen Variants</title>
<link href="https://fonts.googleapis.com/css2?family=Inter:wght@400;500;600&display=swap" rel="stylesheet">
<style>
  :root {
    --stage: #1414e6;
    --brand: #3b36ea;
    --brand-deep: #2f2ad8;
    --header-light: #f7f7f8;
    --body-bg: #eff0f4;
    --card-bg: #f5f5f7;
    --field-border: #dfe2ec;
    --field-text: #5b6fa8;
    --label: #333a4a;
    --muted-tab: #6b7bb0;
    --search-bg: #eef0f5;
    --search-text: #8d97b5;
    --nav-bg: #f7f7f8;
    --icon: #4a4f5c;
    --indicator: #b9bec9;
    --white: #ffffff;
  }
  * { box-sizing: border-box; margin: 0; padding: 0; }
  html, body { width: 1200px; height: 1198px; overflow: hidden; }
  body {
    background: radial-gradient(circle at 50% 45%, #1d1df0 0%, var(--stage) 60%, #1010d8 100%);
    font-family: 'Inter', sans-serif;
    position: relative;
  }
  .screen {
    position: absolute;
    width: 405px;
    height: 880px;
    border-radius: 44px;
    overflow: hidden;
    background: var(--body-bg);
    box-shadow: 0 30px 60px rgba(5, 5, 90, 0.35);
  }
  .screen--light { left: 73px; top: 169px; }
  .screen--brand { left: 715px; top: 166px; }

  .header {
    position: absolute; left: 0; top: 0; width: 100%; height: 197px;
    background: var(--header-light);
  }
  .screen--brand .header { background: var(--brand); }

  .status-time {
    position: absolute; left: 58px; top: 15px; width: 60px; text-align: center;
    font-size: 17px; font-weight: 600; color: #1b1d24;
  }
  .status-icons { position: absolute; right: 30px; top: 18px; }
  .screen--brand .status-time { color: var(--white); }

  .title-bar { position: absolute; left: 0; top: 60px; width: 100%; height: 30px; }
  .title {
    position: absolute; left: 0; right: 0; top: 4px; text-align: center;
    font-size: 17.5px; font-weight: 600; color: var(--brand); letter-spacing: 0.1px;
  }
  .screen--brand .title { color: var(--white); }
  .back-icon { position: absolute; left: 48px; top: 6px; }
  .more-icon { position: absolute; left: 349px; top: 5px; }

  .search {
    position: absolute; left: 28px; top: 119px; width: 348px; height: 41px;
    border-radius: 21px; background: var(--search-bg);
    display: flex; align-items: center; padding-left: 20px; gap: 12px;
    font-size: 13.5px; color: var(--search-text);
  }
  .screen--brand .search { background: var(--white); }

  .card {
    position: absolute; left: 28px; top: 225px; width: 348px; height: 528px;
    border-radius: 20px; background: var(--card-bg);
  }
  .tabs {
    position: absolute; left: 30px; top: 24px; width: 289px; height: 27px;
    border-bottom: 1px solid #e2e4ec;
    font-size: 13.5px;
  }
  .tab { position: absolute; top: 0; transform: translateX(-50%); color: var(--muted-tab); white-space: nowrap; }
  .tab--active { color: var(--brand); font-weight: 500; }
  .tab-underline {
    position: absolute; left: 0; bottom: -1px; width: 96px; height: 2px;
    background: var(--brand); border-radius: 1px;
  }

  .field-label {
    position: absolute; left: 29px; font-size: 13.7px; color: var(--label);
  }
  .field {
    position: absolute; left: 29px; width: 290px; height: 40px;
    border: 1px solid var(--field-border); border-radius: 8px; background: var(--card-bg);
    padding: 0 14px; display: flex; align-items: center;
    font-size: 11.5px; color: var(--field-text);
  }
  .field--multiline { height: 62px; line-height: 18.5px; align-items: center; }

  .save-button {
    position: absolute; left: 29px; top: 459px; width: 290px; height: 41px;
    border-radius: 8px; background: var(--brand);
    color: var(--white); font-size: 15px; font-weight: 500;
    display: flex; align-items: center; justify-content: center;
    box-shadow: 0 14px 22px rgba(59, 54, 234, 0.28);
  }

  .bottom-nav {
    position: absolute; left: 0; top: 782px; width: 100%; height: 98px;
    background: var(--nav-bg); border-radius: 22px 22px 0 0;
  }
  .nav-item { position: absolute; top: 12px; width: 50px; height: 50px; display: flex; align-items: center; justify-content: center; }
  .nav-item--home { left: 34px; border-radius: 50%; background: var(--brand); }
  .nav-item--stats { left: 129px; }
  .nav-item--history { left: 224px; }
  .nav-item--profile { left: 320px; }
  .home-indicator {
    position: absolute; left: 132px; top: 86px; width: 140px; height: 4px;
    border-radius: 2px; background: var(--indicator);
  }
</style>
</head>
<body>

<!-- Light header variant -->
<section class="screen screen--light">
  <header class="header">
    <div class="status-time">9:41</div>
    <svg class="status-icons" width="82" height="14" viewBox="0 0 82 14">
      <g fill="#1b1d24">
        <rect x="0" y="9" width="3" height="4" rx="1"/>
        <rect x="5" y="6" width="3" height="7" rx="1"/>
        <rect x="10" y="3" width="3" height="10" rx="1"/>
        <rect x="15" y="0" width="3" height="13" rx="1"/>
        <path d="M26 4.5a11 11 0 0 1 15 0l-1.6 1.7a8.6 8.6 0 0 0-11.8 0z"/>
        <path d="M29 7.6a6.6 6.6 0 0 1 9 0l-1.6 1.7a4.2 4.2 0 0 0-5.8 0z"/>
        <path d="M31.8 10.6a2.4 2.4 0 0 1 3.4 0L33.5 12.4z"/>
        <rect x="52" y="1.5" width="25" height="11" rx="3" fill="none" stroke="#1b1d24" stroke-opacity="0.4"/>
        <rect x="54" y="3.5" width="21" height="7" rx="1.5"/>
        <rect x="78.5" y="5" width="1.5" height="4" rx="0.7" fill-opacity="0.4"/>
      </g>
    </svg>
    <div class="title-bar">
      <svg class="back-icon" width="14" height="18" viewBox="0 0 14 18"><path d="M10 1 2 9l8 8" fill="none" stroke="#2a2d36" stroke-width="1.8" stroke-linecap="round" stroke-linejoin="round"/></svg>
      <h1 class="title">Development Overview</h1>
      <svg class="more-icon" width="6" height="20" viewBox="0 0 6 20"><g fill="#1b1d24"><circle cx="3" cy="3" r="2.2"/><circle cx="3" cy="10" r="2.2"/><circle cx="3" cy="17" r="2.2"/></g></svg>
    </div>
    <div class="search">
      <svg width="17" height="17" viewBox="0 0 17 17"><g fill="none" stroke="#5b6fa8" stroke-width="1.5" stroke-linecap="round"><circle cx="7" cy="7" r="6"/><path d="M11.5 11.5 16 16"/></g></svg>
      <span>Search for something</span>
    </div>
  </header>

  <main class="card">
    <nav class="tabs">
      <span class="tab tab--active" style="left:48px">General</span>
      <span class="tab" style="left:148px">Compliance</span>
      <span class="tab" style="left:242px">Finances</span>
      <span class="tab-underline"></span>
    </nav>
    <label class="field-label" style="top:76px">Handover date</label>
    <div class="field" style="top:105px">12 januari 2023</div>
    <label class="field-label" style="top:163px">Units</label>
    <div class="field" style="top:192px">85</div>
    <label class="field-label" style="top:250px">Address</label>
    <div class="field field--multiline" style="top:279px">42 Fenwick Garden Road, London,<br>W100 7RL</div>
    <label class="field-label" style="top:359px">Sections 20 limit</label>
    <div class="field" style="top:388px">$20</div>
    <div class="save-button">Save</div>
  </main>

  <footer class="bottom-nav">
    <div class="nav-item nav-item--home">
      <svg width="24" height="24" viewBox="0 0 24 24"><g fill="none" stroke="#fff" stroke-width="1.8" stroke-linejoin="round"><path d="M3 10.5 12 3l9 7.5V21H3z"/><path d="M9.5 21v-6.5h5V21"/></g></svg>
    </div>
    <div class="nav-item nav-item--stats">
      <svg width="26" height="26" viewBox="0 0 26 26"><g fill="none" stroke="#3b36ea" stroke-width="1.9" stroke-linejoin="round"><path d="M11 4.5a10 10 0 1 0 10.5 10.5H11z"/><path d="M14.5 2v9.5H24A9.5 9.5 0 0 0 14.5 2z"/></g></svg>
    </div>
    <div class="nav-item nav-item--history">
      <svg width="26" height="26" viewBox="0 0 26 26"><g fill="none" stroke="#4a4f5c" stroke-width="1.9" stroke-linecap="round"><circle cx="13" cy="13" r="10.5"/><path d="M13 7v6.5l4 2.5"/></g></svg>
    </div>
    <div class="nav-item nav-item--profile">
      <svg width="24" height="26" viewBox="0 0 24 26"><g fill="none" stroke="#4a4f5c" stroke-width="1.9" stroke-linecap="round"><circle cx="12" cy="7" r="5"/><path d="M2 24a10 10 0 0 1 20 0"/></g></svg>
    </div>
    <span class="home-indicator"></span>
  </footer>
</section>

<!-- Brand header variant -->
<section class="screen screen--brand">
  <header class="header">
    <div class="status-time">9:41</div>
    <svg class="status-icons" width="82" height="14" viewBox="0 0 82 14">
      <g fill="#ffffff">
        <rect x="0" y="9" width="3" height="4" rx="1"/>
        <rect x="5" y="6" width="3" height="7" rx="1"/>
        <rect x="10" y="3" width="3" height="10" rx="1"/>
        <rect x="15" y="0" width="3" height="13" rx="1"/>
        <path d="M26 4.5a11 11 0 0 1 15 0l-1.6 1.7a8.6 8.6 0 0 0-11.8 0z"/>
        <path d="M29 7.6a6.6 6.6 0 0 1 9 0l-1.6 1.7a4.2 4.2 0 0 0-5.8 0z"/>
        <path d="M31.8 10.6a2.4 2.4 0 0 1 3.4 0L33.5 12.4z"/>
        <rect x="52" y="1.5" width="25" height="11" rx="3" fill="none" stroke="#ffffff" stroke-opacity="0.5"/>
        <rect x="54" y="3.5" width="21" height="7" rx="1.5"/>
        <rect x="78.5" y="5" width="1.5" height="4" rx="0.7" fill-opacity="0.5"/>
      </g>
    </svg>
    <div class="title-bar">
      <svg class="back-icon" width="14" height="18" viewBox="0 0 14 18"><path d="M10 1 2 9l8 8" fill="none" stroke="#ffffff" stroke-width="1.8" stroke-linecap="round" stroke-linejoin="round"/></svg>
      <h1 class="title">Development Overview</h1>
      <svg class="more-icon" width="6" height="20" viewBox="0 0 6 20"><g fill="#ffffff"><circle cx="3" cy="3" r="2.2"/><circle cx="3" cy="10" r="2.2"/><circle cx="3" cy="17" r="2.2"/></g></svg>
    </div>
    <div class="search">
      <svg width="17" height="17" viewBox="0 0 17 17"><g fill="none" stroke="#5b6fa8" stroke-width="1.5" stroke-linecap="round"><circle cx="7" cy="7" r="6"/><path d="M11.5 11.5 16 16"/></g></svg>
      <span>Search for something</span>
    </div>
  </header>

  <main class="card">
    <nav class="tabs">
      <span class="tab tab--active" style="left:48px">General</span>
      <span class="tab" style="left:148px">Compliance</span>
      <span class="tab" style="left:242px">Finances</span>
      <span class="tab-underline"></span>
    </nav>
    <label class="field-label" style="top:76px">Handover date</label>
    <div class="field" style="top:105px">12 januari 2023</div>
    <label class="field-label" style="top:163px">Units</label>
    <div class="field" style="top:192px">85</div>
    <label class="field-label" style="top:250px">Address</label>
    <div class="field field--multiline" style="top:279px">42 Fenwick Garden Road, London,<br>W100 7RL</div>
    <label class="field-label" style="top:359px">Sections 20 limit</label>
    <div class="field" style="top:388px">$20</div>
    <div class="save-button">Save</div>
  </main>

  <footer class="bottom-nav">
    <div class="nav-item nav-item--home">
      <svg width="24" height="24" viewBox="0 0 24 24"><g fill="none" stroke="#fff" stroke-width="1.8" stroke-linejoin="round"><path d="M3 10.5 12 3l9 7.5V21H3z"/><path d="M9.5 21v-6.5h5V21"/></g></svg>
    </div>
    <div class="nav-item nav-item--stats">
      <svg width="26" height="26" viewBox="0 0 26 26"><g fill="none" stroke="#3b36ea" stroke-width="1.9" stroke-linejoin="round"><path d="M11 4.5a10 10 0 1 0 10.5 10.5H11z"/><path d="M14.5 2v9.5H24A9.5 9.5 0 0 0 14.5 2z"/></g></svg>
    </div>
    <div class="nav-item nav-item--history">
      <svg width="26" height="26" viewBox="0 0 26 26"><g fill="none" stroke="#4a4f5c" stroke-width="1.9" stroke-linecap="round"><circle cx="13" cy="13" r="10.5"/><path d="M13 7v6.5l4 2.5"/></g></svg>
    </div>
    <div class="nav-item nav-item--profile">
      <svg width="24" height="26" viewBox="0 0 24 26"><g fill="none" stroke="#4a4f5c" stroke-width="1.9" stroke-linecap="round"><circle cx="12" cy="7" r="5"/><path d="M2 24a10 10 0 0 1 20 0"/></g></svg>
    </div>
    <span class="home-indicator"></span>
  </footer>
</section>

</body>
</html>
```